Vista Bay - Aged Care

We would like a multipage brochure for the healthcare market. Specifically for Aged Care, not so much hospitals though.
I have supplied information from a website that has all the feature but we need it with our look & feel. See our corporate capability brochure for design elements. We would like the features to be seen graphically (see Feature Image.pdf as a wireframe example. See KRNwave for information regarding RTLS (KRNwave) (This is an important feature we want to push. See our current hospital brochure (Healthcare), it also has KRNwave. The rest of the information can be derived from the website https://www.qlvx-example.com/screen-range/pro-sets/vistabay

Target Market(s)

Aged Care or Assisted Living

Industry/Entity Type

Aged Care

Font styles to use
Other font styles liked:
• Lato-Black, Lato-Bold, Lato-Regulat, Poppins-Bold, Poppins, Regular, Poppins- SemiBold

Colors

Designer to choose colors to be used in the design.

Requirements
Must have
• KRN Logo
Nice to have
• We would really like an image with the features mentioned around the TV, Folloed by a point for like our Hospital Brochure. Please also use our corporate colours in the two brochures.

```html
<!DOCTYPE html>
<html lang="en">
<head>
<meta charset="utf-8">
<title>Vista Bay – Aged Care Brochure</title>
<link rel="stylesheet" href="https://fonts.googleapis.com/css2?family=Poppins:wght@400;500;600;700;800&family=Oswald:wght@600;700&family=Montserrat:wght@500;700;800&display=swap">
<style>
  :root {
    --backdrop: #cfd0cb;
    --paper: #ffffff;
    --brand-blue: #0f4f98;
    --brand-orange: #f26b0f;
    --ink: #1c1c1c;
    --pill-start: #1a3f78;
    --pill-end: #2aa3d6;
  }
  * { margin: 0; padding: 0; box-sizing: border-box; }
  html, body { width: 1200px; height: 1010px; overflow: hidden; background: var(--backdrop); }
  .canvas { position: relative; width: 1200px; height: 1010px; }

  .page {
    position: absolute; top: 202px; width: 502px; height: 648px;
    background: var(--paper); overflow: hidden;
    box-shadow: 0 6px 18px rgba(0,0,0,.12);
  }
  .page--cover { left: 71px; }
  .page--features { left: 638px; }
  .page__art { position: absolute; inset: 0; width: 502px; height: 648px; }

  .brand-name {
    position: absolute; left: 33px; top: 40px;
    font-family: "Poppins", sans-serif; font-weight: 700; font-size: 40px;
    line-height: 1; color: var(--brand-blue); letter-spacing: 1px;
  }

  .cover-title { position: absolute; left: 0; right: 0; top: 484px; text-align: center; }
  .cover-title__lead {
    font-family: "Poppins", sans-serif; font-weight: 400; font-size: 21px;
    letter-spacing: 6px; color: var(--ink); line-height: 26px;
  }
  .cover-title__main {
    font-family: "Montserrat", sans-serif; font-weight: 800; font-size: 25.5px;
    color: var(--brand-blue); line-height: 28px; margin-top: 1px;
  }
  .cover-title__accent {
    font-family: "Oswald", sans-serif; font-weight: 700; font-size: 37px;
    color: var(--brand-orange); line-height: 40px; letter-spacing: 0.3px;
  }
  .divider-dots { position: absolute; left: 224px; top: 590px; display: flex; gap: 5px; }
  .divider-dots span { width: 6px; height: 6px; background: var(--brand-blue); }
  .divider-dots span:first-child, .divider-dots span:last-child { opacity: .45; }
  .cover-url {
    position: absolute; left: 0; right: 0; top: 604px; text-align: center; white-space: nowrap;
    font-family: "Montserrat", sans-serif; font-weight: 700; font-size: 16px;
    letter-spacing: 3px; color: var(--ink);
  }

  .section-title { position: absolute; left: 31px; top: 305px; }
  .section-title__top {
    font-family: "Oswald", sans-serif; font-weight: 700; font-size: 35px;
    line-height: 36px; color: var(--brand-blue);
  }
  .section-title__bottom {
    font-family: "Montserrat", sans-serif; font-weight: 800; font-size: 26px;
    line-height: 32px; color: var(--brand-orange); letter-spacing: .5px;
  }
  .intro-copy {
    position: absolute; left: 31px; top: 376px; width: 210px;
    font-family: "Montserrat", sans-serif; font-weight: 500; font-size: 8.8px;
    line-height: 10.8px; color: var(--ink);
  }

  .feature-heading {
    position: absolute; left: 268px; top: 356px; white-space: nowrap;
    font-family: "Montserrat", sans-serif; font-weight: 800; font-size: 15px;
    color: var(--brand-blue); letter-spacing: .2px;
  }
  .feature-heading span { color: var(--brand-orange); }

  .feature-pill {
    position: absolute; height: 20px; border-radius: 0 10px 10px 0;
    background: linear-gradient(90deg, var(--pill-start), var(--pill-end));
    font-family: "Poppins", sans-serif; font-weight: 600; font-size: 11px;
    line-height: 20px; color: #fff; padding-left: 11px; white-space: nowrap;
  }
  .feature-icon {
    position: absolute; width: 32px; height: 32px; border-radius: 50%;
    background: var(--pill-start); border: 2px solid #fff;
    box-shadow: 0 0 0 1px var(--pill-start);
  }
  .feature-icon svg { position: absolute; left: 5px; top: 5px; width: 18px; height: 18px; }
  .feature-copy {
    position: absolute; width: 202px;
    font-family: "Montserrat", sans-serif; font-weight: 500; font-size: 9.4px;
    line-height: 12px; color: var(--ink);
  }
  .feature-url {
    position: absolute; right: 32px; top: 612px; white-space: nowrap;
    font-family: "Montserrat", sans-serif; font-weight: 700; font-size: 8.5px;
    letter-spacing: 1.4px; color: var(--ink);
  }
</style>
</head>
<body>
<div class="canvas">

  <section class="page page--cover">
    <svg class="page__art" viewBox="0 0 836 1081" preserveAspectRatio="none">
      <defs>
        <linearGradient id="careGradient" x1="0" y1="0" x2="1" y2="1">
          <stop offset="0" stop-color="#e6cfb4"/>
          <stop offset="0.35" stop-color="#c79f7c"/>
          <stop offset="0.55" stop-color="#7aa6d2"/>
          <stop offset="0.75" stop-color="#c8b3a6"/>
          <stop offset="1" stop-color="#9a8a7c"/>
        </linearGradient>
        <radialGradient id="careGlow" cx="0.55" cy="0.55" r="0.5">
          <stop offset="0" stop-color="#5f93c8" stop-opacity=".55"/>
          <stop offset="1" stop-color="#5f93c8" stop-opacity="0"/>
        </radialGradient>
      </defs>
      <g role="img" aria-label="Photo: carer in scrubs comforting an elderly resident in a wheelchair in an aged care lounge">
        <path d="M241 214 C400 70 620 26 836 24 V560 C700 650 520 742 340 744 C150 746 70 600 110 430 C135 330 190 262 241 214 Z" fill="url(#careGradient)"/>
        <path d="M241 214 C400 70 620 26 836 24 V560 C700 650 520 742 340 744 C150 746 70 600 110 430 C135 330 190 262 241 214 Z" fill="url(#careGlow)"/>
      </g>
      <path d="M241 200 C400 58 620 8 836 6" fill="none" stroke="var(--brand-orange)" stroke-width="16"/>
      <path d="M98 400 C40 610 150 782 360 776 C560 770 720 684 836 592" fill="none" stroke="var(--brand-blue)" stroke-width="17"/>
    </svg>
    <div class="brand-name">QLVX</div>

    <div class="cover-title">
      <div class="cover-title__lead">OPTIMISE YOUR</div>
      <div class="cover-title__main">AGED CARE EXPERIENCE WITH</div>
      <div class="cover-title__accent">REAL-TIME LOCATION SYSTEMS</div>
    </div>
    <div class="divider-dots"><span></span><span></span><span></span><span></span><span></span></div>
    <div class="cover-url">www.qlvx-example.com</div>
  </section>

  <section class="page page--features">
    <svg class="page__art" viewBox="0 0 836 1081" preserveAspectRatio="none">
      <defs>
        <linearGradient id="teamGradient" x1="0" y1="0" x2="1" y2="1">
          <stop offset="0" stop-color="#4f7fae"/>
          <stop offset="0.4" stop-color="#15355a"/>
          <stop offset="0.7" stop-color="#2c5f93"/>
          <stop offset="1" stop-color="#0f2c4c"/>
        </linearGradient>
        <radialGradient id="teamGlow" cx="0.5" cy="0.45" r="0.35">
          <stop offset="0" stop-color="#dfe8f2" stop-opacity=".55"/>
          <stop offset="1" stop-color="#dfe8f2" stop-opacity="0"/>
        </radialGradient>
        <linearGradient id="residentGradient" x1="0" y1="0" x2="1" y2="0">
          <stop offset="0" stop-color="#8fa8c4"/>
          <stop offset="0.45" stop-color="#efc9b3"/>
          <stop offset="0.8" stop-color="#f4e6dc"/>
          <stop offset="1" stop-color="#ffffff" stop-opacity="0"/>
        </linearGradient>
      </defs>
      <g role="img" aria-label="Photo: care team reviewing information on a large interactive display in a modern facility">
        <path d="M10 0 H836 V350 C760 436 600 474 440 472 C230 468 40 370 0 150 V10 Z" fill="url(#teamGradient)"/>
        <path d="M10 0 H836 V350 C760 436 600 474 440 472 C230 468 40 370 0 150 V10 Z" fill="url(#teamGlow)"/>
      </g>
      <path d="M0 150 C40 400 230 508 440 510 C620 512 770 452 836 362 V350 C760 440 600 486 440 484 C230 480 40 380 0 190 Z" fill="var(--brand-orange)"/>
      <path role="img" aria-label="Photo: smiling elderly resident resting in bed using a tablet"
            d="M0 820 C60 790 120 790 180 800 C300 820 380 880 420 960 C440 1010 450 1050 460 1081 H0 Z"
            fill="url(#residentGradient)"/>
    </svg>

    <div class="section-title">
      <div class="section-title__top">CARE AND</div>
      <div class="section-title__bottom">CONNECTIVITY</div>
    </div>
    <p class="intro-copy">Optimise your patient experience. Norvane professional display solutions enables healthcare facilities such as hospitals, doctor’s offices, and clinics to streamline their processes with smart technology. From antimicrobial display housing to advanced connectivity, every detail is covered to help you provide better treatment.</p>

    <div class="feature-heading">ENHANCING <span>HEALTHCARE</span></div>

    <div class="feature-pill" style="left:298px; top:388px; width:167px;">Healthcare compliant</div>
    <div class="feature-icon" style="left:266px; top:382px;">
      <svg viewBox="0 0 24 24" fill="none" stroke="#fff" stroke-width="1.6" stroke-linejoin="round">
        <path d="M12 20 C4 14 2 10 4 6.5 C6 3.5 10 4 12 7 C14 4 18 3.5 20 6.5 C21 8.5 20.5 10.5 19 12.5"/>
        <path d="M4 12 H8 L9.5 9 L11.5 14 L13 12 H15"/>
        <circle cx="18" cy="17" r="3.4" stroke="var(--brand-orange)"/>
        <path d="M18 15.3 V18.7 M16.3 17 H19.7" stroke="var(--brand-orange)"/>
      </svg>
    </div>
    <p class="feature-copy" style="left:268px; top:421px;">Impede the spread of germs and your keep patients safer with healthcare compliant antimicrobial casing and toughened hydrophobic glass front.</p>

    <div class="feature-pill" style="left:294px; top:489px; width:154px;">Patient comfort</div>
    <div class="feature-icon" style="left:262px; top:483px;">
      <svg viewBox="0 0 24 24" fill="none" stroke="#fff" stroke-width="1.6" stroke-linejoin="round">
        <path d="M3 6 V19 M3 15 H21 V19"/>
        <rect x="8" y="10.5" width="12" height="4.5" rx="1"/>
        <circle cx="5.8" cy="12" r="1.6"/>
        <path d="M14 3 H18 V8 H14 Z" stroke="var(--brand-orange)"/>
      </svg>
    </div>
    <p class="feature-copy" style="left:264px; top:521px;">CastLink built-in and access to the App Hub store keeps patients happier and more comfortable during times of stress and recovery.</p>

    <div class="feature-url">www.qlvx-example.com</div>
  </section>

</div>
</body>
</html>
```